Web Design Project

The Varnholt Group is a strategy consulting group that works primarily with the healthcare industry. We provide a limited range of strategic planning & marketing services designed to focus on the growth and future viability of our clients’ organizations. We are a very small organization, but want to communicate a sense of boldness, forward-looking/visionary, and both creative and analytic. What follows below is: 1) A simple overview of the outline of the web-pages; 2) an important list of web-sites that appeal to me – the most important of which appears in a larger font; 3) photo ideas for the home page (from Pictavo.com). I have not written copy…and won’t until I know length based upon design.

The Varnholt Group
Healthcare Strategic Consulting

(Key Sections for the site)
HOME PAGE ABOUT US SERVICES NEWS & COMMENTS CONTACT US

(Sites That I Admire:)

http://www.lumenwirk.eu/services/ Very creative use of iconography to represent services, etc.

http://quillmoss.com/ Arresting graphics

http://brontiva.co/ GREAT SITE. THIS IS THE SITE THAT I LIKE THE MOST IN TERMS OF GENERAL LOOK & FEEL.

http://kasperholm.com/ Very interesting, stark/bold B&W site for architects

http://www.rtmalvey.com/ Interesting home page for promoting individual

HOME PAGE:

The Varnholt Group
STRATEGIC CONSULTING SERVICES (should be bold). We have a Logo that can be supplied later

Pictavo Image Options: 47193652, 36840157, 29617483, 58302619, 274815936, 61948237
Updates

Project Deadline Extended
Reason: The 1st and 2nd place designers will have an additional 5-7 days to complete the remaining pages of the site (approximately 11 pages). I have a file with all the photo information and rough copy that can be dropped into position.

Target Market(s)

Senior Executives (CEO,COO, CFO,SVP) in major hospitals or healthcare systems, other senior executives within healthcare.

Industry/Entity Type

Healthcare

Requirements
Must have
• I will want to pay to have this project expanded to show look and feel for:
*Home Page and key sections
*4 Pages that will be under the "About Us" heading
*5 Pages that will be under the "Services" heading

I have image options selected from Pictavo for all key sections. We will need to look at the cost for those images that the designer recommends.

```html
<!DOCTYPE html>
<html lang="en">
<head>
<meta charset="utf-8">
<title>The Varnholt Group — Strategic Consulting Services</title>
<link href="https://fonts.googleapis.com/css2?family=Figtree:wght@400;500;600;700&display=swap" rel="stylesheet">
<style>
  :root {
    --ink: #1f1f1f;
    --text: #3a3a3a;
    --brand-red: #c0201f;
    --navy: #27418a;
    --nav-dark: #333536;
    --nav-frame: #d2d2d2;
    --accent-gold: #c9c23a;
    --band-grey: #ebebeb;
    --footer: #4a4a4a;
    --white: #ffffff;
  }
  * { margin: 0; padding: 0; box-sizing: border-box; }
  html, body { width: 894px; height: 1200px; overflow: hidden; }
  body {
    position: relative;
    font-family: "Figtree", "Helvetica Neue", Arial, sans-serif;
    color: var(--text);
    background: var(--white);
  }
  .hero {
    position: absolute; left: 0; top: 0; width: 894px; height: 627px;
    background:
      linear-gradient(180deg, #e4ecea 0%, #d6e4e0 45%, #c3d6d1 75%, #7f938c 100%);
  }
  .hero-figures {
    position: absolute; left: 480px; top: 260px; width: 300px; height: 310px;
    background: radial-gradient(ellipse at center, rgba(40,45,45,.55) 0%, rgba(40,45,45,0) 70%);
  }
  .site-header {
    position: absolute; left: 0; top: 30px; width: 894px; height: 72px;
    background: rgba(255,255,255,.88);
  }
  .brand { position: absolute; left: 90px; top: 16px; }
  .brand-name {
    font-size: 23px; font-weight: 600; color: var(--brand-red); letter-spacing: -.2px; line-height: 1;
  }
  .brand-tag {
    margin-top: 5px; font-size: 9.6px; font-weight: 700; color: var(--ink); letter-spacing: .2px;
  }
  .main-nav {
    position: absolute; left: 374px; top: 12px; width: 429px; height: 50px;
    background: var(--nav-frame); border-radius: 4px; padding: 5px 6px;
  }
  .main-nav ul {
    display: flex; list-style: none; height: 100%;
    background: linear-gradient(180deg, #444748 0%, var(--nav-dark) 100%);
    border-radius: 2px;
  }
  .main-nav li {
    position: relative; display: flex; align-items: center; justify-content: center;
    font-size: 8.8px; letter-spacing: .9px; color: #e8e8e8; border-right: 1px solid #555;
  }
  .main-nav li:last-child { border-right: 0; }
  .main-nav li.current { color: var(--white); font-weight: 600; }
  .main-nav li.current::after {
    content: ""; position: absolute; bottom: 0; left: 50%; margin-left: -11px;
    border-left: 11px solid transparent; border-right: 11px solid transparent;
    border-bottom: 7px solid var(--accent-gold);
  }
  .hero-caption {
    position: absolute; left: 90px; top: 500px; width: 714px; height: 98px;
    background: rgba(245,245,243,.9);
  }
  .hero-caption p {
    position: absolute; left: 86px; top: 16px; width: 560px;
    font-size: 17.6px; line-height: 22.4px; color: #2a2a2a;
  }
  .hero-arrow { position: absolute; top: 34px; }
  .hero-arrow.prev { left: 26px; }
  .hero-arrow.next { right: 28px; }

  .about { position: absolute; left: 90px; top: 660px; width: 358px; }
  .section-title { font-size: 19.5px; font-weight: 500; color: var(--ink); letter-spacing: .2px; }
  .about .lead { margin-top: 18px; font-size: 12.2px; line-height: 16.1px; color: var(--ink); }
  .about .body { font-size: 9.8px; line-height: 13.6px; }
  .about .body.p1 { margin-top: 15px; }
  .about .body.p2 { margin-top: 19px; padding-left: 3px; }
  .about .body.p3 { margin-top: 21px; padding-left: 3px; }

  .services { position: absolute; left: 499px; top: 666px; width: 306px; }
  .service { position: relative; height: 95px; padding-left: 63px; }
  .service-icon { position: absolute; left: 0; top: 2px; }
  .service h3 { font-size: 12.2px; font-weight: 600; color: var(--ink); }
  .service p { margin-top: 4px; font-size: 8.4px; line-height: 12.2px; }

  .portfolio-band {
    position: absolute; left: 0; top: 967px; width: 894px; height: 188px; background: var(--band-grey);
  }
  .portfolio-photo {
    position: absolute; left: 90px; top: 20px; width: 236px; height: 150px;
    background: var(--white); padding: 5px;
  }
  .portfolio-photo div {
    width: 100%; height: 100%;
    background: linear-gradient(120deg, #8c8f8c 0%, #3e3f41 45%, #2a2b2e 70%, #b8b6b0 100%);
  }
  .portfolio-copy { position: absolute; left: 352px; top: 22px; width: 455px; }
  .portfolio-copy p { margin-top: 11px; font-size: 8.6px; line-height: 11.6px; }
  .portfolio-copy p + p { margin-top: 11px; }
  .learn-more { display: inline-block; margin-top: 9px; font-size: 8.6px; color: var(--brand-red); text-decoration: none; }

  .site-footer {
    position: absolute; left: 0; top: 1155px; width: 894px; height: 45px; background: var(--footer);
    color: var(--white); font-size: 8.4px; font-weight: 500;
  }
  .footer-nav { position: absolute; left: 94px; top: 17px; display: flex; list-style: none; }
  .footer-nav li { margin-right: 12px; }
  .footer-nav li::before { content: "›"; margin-right: 6px; font-size: 9px; }
  .copyright { position: absolute; right: 90px; top: 17px; }
</style>
</head>
<body>
  <div class="hero" role="img" aria-label="Photo: two businessmen shaking hands in silhouette before a whiteboard with a hand-drawn strategy diagram">
    <div class="hero-figures"></div>
  </div>

  <header class="site-header">
    <div class="brand">
      <div class="brand-name">The Varnholt Group</div>
      <div class="brand-tag">STRATEGIC CONSULTING SERVICES</div>
    </div>
    <nav class="main-nav">
      <ul>
        <li class="current" style="width:63px">HOME</li>
        <li style="width:72px">ABOUT US</li>
        <li style="width:72px">SERVICES</li>
        <li style="width:121px">NEWS &amp; COMMENTS</li>
        <li style="width:89px">CONTACT US</li>
      </ul>
    </nav>
  </header>

  <div class="hero-caption">
    <svg class="hero-arrow prev" width="16" height="28" viewBox="0 0 16 28"><path d="M13 3 L3 14 L13 25" fill="none" stroke="#2a2a2a" stroke-width="3.5"/></svg>
    <p>We provide a limited range of strategic planning &amp; marketing services designed to focus on the growth and future viability of our clients’ organizations.</p>
    <svg class="hero-arrow next" width="16" height="28" viewBox="0 0 16 28"><path d="M3 3 L13 14 L3 25" fill="none" stroke="#2a2a2a" stroke-width="3.5"/></svg>
  </div>

  <section class="about">
    <h2 class="section-title">ABOUT US</h2>
    <p class="lead">The Varnholt Group is a strategy consulting group that works primarily with the healthcare industry. We provide a limited range of strategic planning &amp; marketing services designed to focus on the growth and future viability of our clients’ organi-zations.</p>
    <p class="body p1">Lorem ipsum dolor sit amet, consectetur adipiscing elit. Etiam eu ante non dui pharetra accumsan at id diam. Integer porttitor tellus nec metus dictum placerat.</p>
    <p class="body p2">Sed quis enim odio. In a neque eget lacus tincidunt elementum eget et tortor. Fusce iaculis pulvinar magna, vitae dictum sapien ornare id. Phasellus cursus.</p>
    <p class="body p3">Sed quis enim odio. In a neque eget lacus tincidunt elementum eget et tortor.</p>
  </section>

  <section class="services">
    <div class="service">
      <svg class="service-icon" width="46" height="42" viewBox="0 0 46 42">
        <rect x="15" y="1" width="16" height="8" rx="2" fill="none" stroke="#27418a" stroke-width="3"/>
        <rect x="1" y="7" width="44" height="34" rx="3" fill="#27418a"/>
        <rect x="1" y="17" width="44" height="2" fill="#fff"/>
        <path d="M20 21h6v5h5v6h-5v5h-6v-5h-5v-6h5z" fill="#fff"/>
      </svg>
      <h3>HEALTHCARE CONSULTANT</h3>
      <p>Lorem ipsum dolor sit amet, consectetur adipiscing elit. Etiam eu ante non dui pharetra accumsan at id diam. Integer porttitor tellus nec metus dictum placerat. Sed quis enim odio. In a neque eget lacus tincidunt elementum eget et tortor.</p>
    </div>
    <div class="service">
      <svg class="service-icon" width="46" height="48" viewBox="0 0 46 48">
        <path d="M10 3 C4 6 4 16 8 22 C11 27 17 27 20 22 C24 16 24 6 18 3" fill="none" stroke="#27418a" stroke-width="2.6"/>
        <path d="M14 26 C14 38 18 46 27 46 C36 46 40 40 38 30 C37 25 34 24 32 24" fill="none" stroke="#27418a" stroke-width="2.6"/>
        <circle cx="31" cy="17" r="4" fill="#27418a"/>
        <circle cx="10" cy="3" r="2" fill="#27418a"/><circle cx="18" cy="3" r="2" fill="#27418a"/>
      </svg>
      <h3>NEW SERVICES</h3>
      <p>Lorem ipsum dolor sit amet, consectetur adipiscing elit. Etiam eu ante non dui pharetra accumsan at id diam. Integer porttitor tellus nec metus dictum placerat. Sed quis enim odio. In a neque eget lacus tincidunt elementum eget et tortor.</p>
    </div>
    <div class="service">
      <svg class="service-icon" width="46" height="46" viewBox="0 0 46 46">
        <path d="M15 1h16v14h14v16h-14v14h-16v-14h-14v-16h14z" fill="#27418a"/>
        <path d="M19 5h8v14h14v8h-14v14h-8v-14h-14v-8h14z" fill="#fff"/>
        <path d="M21 7h4v14h14v4h-14v14h-4v-14h-14v-4h14z" fill="#27418a"/>
      </svg>
      <h3>MEDICAL SUPPORT</h3>
      <p>Lorem ipsum dolor sit amet, consectetur adipiscing elit. Etiam eu ante non dui pharetra accumsan at id diam. Integer porttitor tellus nec metus dictum placerat. Sed quis enim odio. In a neque eget lacus tincidunt elementum eget et tortor.</p>
    </div>
  </section>

  <section class="portfolio-band">
    <div class="portfolio-photo"><div role="img" aria-label="Photo: three business professionals in suits standing together"></div></div>
    <div class="portfolio-copy">
      <h2 class="section-title">COMPANY PORTFOLIO</h2>
      <p>Lorem ipsum dolor sit amet, consectetur adipiscing elit. Phasellus eu tellus vitae justo mattis pharetra. Lorem ipsum dolor sit amet, consectetur adipiscing elit. Pellentesque pulvinar fringilla ligula, ut cursus justo consectetur nec. Donec ut turpis a nisi mollis venenatis. In cursus volutpat tortor eget iaculis. Maecenas ac ipsum consequat neque porttitor venenatis. Nullam quis purus metus.</p>
      <p>Nam vel libero eu urna vehicula lobortis non nec justo. Proin ultricies aliquet arcu, fermentum interdum nunc dignissim eget. Aliquam eget libero quam. Sed vitae urna lacinia metus euismod volutpat. Cum sociis natoque penatibus et magnis dis parturient montes, nascetur ridiculus mus.</p>
      <a class="learn-more" href="#">Learn More &gt;&gt;</a>
    </div>
  </section>

  <footer class="site-footer">
    <ul class="footer-nav">
      <li>HOME</li><li>ABOUT US</li><li>SERVICES</li><li>NEWS &amp; COMMENTS</li><li>CONTACT US</li>
    </ul>
    <div class="copyright">The Varnholt Group © 2012</div>
  </footer>
</body>
</html>
```